Substance abuse awareness flyer for school age kids

I am needing a flyer for school-age kids. What if it were designed to look like an Travlo with someone texting and the text bubbles were some of the text below with emojis? Maybe a text chain between to friends:

Maybe the first text bubble says "I'm thinking about using drugs and alcohol"
the next bubble: "Just say no!" ( perhaps a stop sign emoji ?)

"Talk to your parents, your teachers at school, or your doctor about how drugs and alcohol can harm you"

another text bubble "did you know that alcohol and drugs could lead to..."
then include some of the info below (see links for more info).
Where ever you get info, it must be cited.

this needs to be English on one side and Spanish on the other side and needs to include the logo attached.

The effects of substance abuse
BWR: https://www.bwr-example.org/kvtmpl/yrnq/articles/youth-risk-habits.html
Affect growth and development, especially brain development. Not able to focus at school or be around friends. https://www.healthyminds-sample.org/pages/shared/docs/stayingclear_2.pdf
Leads to risky behaviors and lack of impulse control (dangerous activities) https://www.healthyminds-sample.org/pages/shared/docs/stayingclear_2.pdf
Contribute to health problems as an adult: heart disease, high blood pressure, and trouble sleeping.

Target Market(s)

school age kids 9-20

Requirements
Must have
• Print ready: 8.5x11

```html
<!DOCTYPE html>
<html lang="en">
<head>
<meta charset="utf-8">
<title>The Effects of Substance Abuse – Flyer</title>
<link href="https://fonts.googleapis.com/css2?family=Montserrat:wght@400;800&family=Oswald:wght@300;400&display=swap" rel="stylesheet">
<style>
  :root{
    --page-bg:#e4e4e4;
    --brand-blue:#0a6cf5;
    --paper:#ffffff;
    --phone-frame:#333333;
    --screen-en:#ffcc33;
    --screen-es:#ff2e63;
    --bubble-blue:#0a6cf5;
    --bubble-green:#11cc00;
    --avatar-dark:#333333;
    --avatar-light:#ffffff;
    --stop-red:#e52521;
    --ref-grey:#cccccc;
    --ref-text:#555555;
    --ink:#333333;
  }
  *{box-sizing:border-box;margin:0;padding:0}
  html,body{width:1200px;height:1200px;overflow:hidden}
  body{background:var(--page-bg);position:relative;font-family:'Oswald',sans-serif}

  .flyer{position:absolute;left:211px;top:50px;width:778px;height:1100px;background:var(--paper);overflow:hidden}
  .flyer__band{position:absolute;inset:0;width:778px;height:1100px}

  .flyer__title{position:absolute;left:64px;top:70px;font-family:'Montserrat',sans-serif;font-weight:800;
    font-size:52px;line-height:60px;color:var(--paper);letter-spacing:1px}

  .brand{position:absolute;left:599px;top:37px;width:140px;height:140px;border-radius:50%;
    background:var(--paper);display:flex;align-items:center;justify-content:center;text-align:center;padding:18px}
  .brand__name{font-family:'Oswald',sans-serif;font-weight:400;font-size:17px;line-height:20px;color:var(--ink);text-transform:uppercase}

  .phone{position:absolute;top:288px;width:311px;height:637px;border-radius:58px;background:var(--phone-frame)}
  .phone--en{left:66px}
  .phone--es{left:416px}
  .phone__screen{position:absolute;left:13px;top:13px;right:13px;bottom:13px;border-radius:46px}
  .phone--en .phone__screen{background:var(--screen-en)}
  .phone--es .phone__screen{background:var(--screen-es)}
  .phone__notch{position:absolute;left:78px;top:0;width:155px;height:36px;background:var(--phone-frame);border-radius:0 0 22px 22px}
  .phone__speaker{position:absolute;left:55px;top:19px;width:40px;height:4px;border-radius:2px;background:var(--paper)}
  .phone__camera{position:absolute;left:102px;top:17px;width:8px;height:8px;border-radius:50%;background:var(--paper)}
  .phone__time{position:absolute;left:40px;top:22px;font-family:'Montserrat',sans-serif;font-size:9px;color:#555}
  .phone__status{position:absolute;right:32px;top:24px}

  .bubble{position:absolute;font-family:'Oswald',sans-serif;font-weight:300;font-size:14px;line-height:18.3px;
    color:var(--paper);padding:6px 9px;border-radius:10px}
  .bubble--sent{left:113px;top:62px;width:172px;height:47px;background:var(--bubble-green);border-radius:12px}
  .bubble--reply{left:28px;width:173px;background:var(--bubble-blue)}
  .bubble--reply::after{content:"";position:absolute;right:-14px;top:14px;width:22px;height:14px;
    border-top:8px solid var(--bubble-blue);border-radius:0 16px 0 0}
  .bubble--sent::before{content:"";position:absolute;left:-14px;top:18px;width:22px;height:14px;
    border-top:8px solid var(--bubble-green);border-radius:16px 0 0 0}

  .avatar{position:absolute;width:54px;height:54px;border-radius:50%}
  .avatar--sender{left:36px;top:63px;background:var(--avatar-light)}
  .avatar--friend{left:223px;background:var(--avatar-dark)}

  .stop-icon{position:absolute;left:94px;top:4px}

  .references{position:absolute;left:64px;top:948px;width:666px;height:190px;border-radius:24px;background:var(--ref-grey);padding:26px 40px}
  .references__label{font-family:'Oswald',sans-serif;font-weight:400;font-size:14px;color:var(--ink);margin-bottom:9px}
  .references__list{list-style:none;font-family:'Montserrat',sans-serif;font-size:12.6px;line-height:18.5px;color:var(--ref-text)}
</style>
</head>
<body>
<main class="flyer">
  <svg class="flyer__band" viewBox="0 0 778 1100" aria-hidden="true">
    <polygon points="0,0 778,0 778,615 0,725" fill="var(--brand-blue)"/>
  </svg>

  <h1 class="flyer__title">THE EFFECTS<br>OF SUBSTANCE<br>ABUSE</h1>

  <div class="brand"><span class="brand__name">Riverbend Wellness Group</span></div>

  <!-- English conversation -->
  <section class="phone phone--en" lang="en">
    <div class="phone__screen">
      <span class="phone__time">22:47</span>
      <svg class="phone__status" width="34" height="8" viewBox="0 0 34 8" aria-hidden="true">
        <path d="M0 3 Q5 -1 10 3 L5 8 Z" fill="#555"/><rect x="14" y="1" width="18" height="6" rx="1.5" fill="#555"/>
      </svg>
      <div class="avatar avatar--sender" role="img" aria-label="Profile icon of the texting friend"></div>
      <p class="bubble bubble--sent">I'm thinking about using drugs and alcohol</p>

      <p class="bubble bubble--reply" style="top:119px;height:47px">Just say no!
        <svg class="stop-icon" width="34" height="34" viewBox="0 0 34 34" aria-hidden="true">
          <polygon points="10,1 24,1 33,10 33,24 24,33 10,33 1,24 1,10" fill="var(--paper)"/>
          <polygon points="11,4 23,4 30,11 30,23 23,30 11,30 4,23 4,11" fill="var(--stop-red)"/>
        </svg>
      </p>
      <div class="avatar avatar--friend" role="img" aria-label="Profile icon of the replying friend" style="top:116px"></div>

      <p class="bubble bubble--reply" style="top:179px;height:86px">Talk to your parents, your teachers at school, or your doctor about how drugs and alcohol can harm you</p>
      <div class="avatar avatar--friend" role="img" aria-label="Profile icon of the replying friend" style="top:178px"></div>

      <p class="bubble bubble--reply" style="top:278px;height:48px">did you know that alcohol and drugs could lead to..</p>
      <div class="avatar avatar--friend" role="img" aria-label="Profile icon of the replying friend" style="top:275px"></div>

      <p class="bubble bubble--reply" style="top:337px;height:100px">effect growth and development, especially brain development. Not able to focus at school or be around friends.</p>
      <div class="avatar avatar--friend" role="img" aria-label="Profile icon of the replying friend" style="top:334px"></div>

      <p class="bubble bubble--reply" style="top:449px;height:48px">risky behaviors and lack of impulse control</p>
      <div class="avatar avatar--friend" role="img" aria-label="Profile icon of the replying friend" style="top:446px"></div>

      <p class="bubble bubble--reply" style="top:508px;height:82px">health problems as an adult: heart disease, high blood pressure, and trouble sleeping.</p>
      <div class="avatar avatar--friend" role="img" aria-label="Profile icon of the replying friend" style="top:506px"></div>
    </div>
    <div class="phone__notch"><span class="phone__speaker"></span><span class="phone__camera"></span></div>
  </section>

  <!-- Spanish conversation -->
  <section class="phone phone--es" lang="es">
    <div class="phone__screen">
      <span class="phone__time">22:47</span>
      <svg class="phone__status" width="34" height="8" viewBox="0 0 34 8" aria-hidden="true">
        <path d="M0 3 Q5 -1 10 3 L5 8 Z" fill="#555"/><rect x="14" y="1" width="18" height="6" rx="1.5" fill="#555"/>
      </svg>
      <div class="avatar avatar--sender" role="img" aria-label="Ícono de perfil del amigo que escribe"></div>
      <p class="bubble bubble--sent">Estoy pensando en consumir drogas y alcohol</p>

      <p class="bubble bubble--reply" style="top:119px;height:47px">¡Solo di no!
        <svg class="stop-icon" width="34" height="34" viewBox="0 0 34 34" aria-hidden="true">
          <polygon points="10,1 24,1 33,10 33,24 24,33 10,33 1,24 1,10" fill="var(--paper)"/>
          <polygon points="11,4 23,4 30,11 30,23 23,30 11,30 4,23 4,11" fill="var(--stop-red)"/>
        </svg>
      </p>
      <div class="avatar avatar--friend" role="img" aria-label="Ícono de perfil del amigo que responde" style="top:116px"></div>

      <p class="bubble bubble--reply" style="top:179px;height:86px">Habla con tus padres, tus maestros en la escuela o tu médico sobre cómo las drogas y el alcohol hacerte daño.</p>
      <div class="avatar avatar--friend" role="img" aria-label="Ícono de perfil del amigo que responde" style="top:178px"></div>

      <p class="bubble bubble--reply" style="top:278px;height:48px">¿Sabías que el alcohol y las drogas pueden provocar ..</p>
      <div class="avatar avatar--friend" role="img" aria-label="Ícono de perfil del amigo que responde" style="top:275px"></div>

      <p class="bubble bubble--reply" style="top:337px;height:100px">afectar el crecimiento y el desarrollo, especialmente el desarrollo del cerebro. No poder concentrarse en la escuela o estar con amigos.</p>
      <div class="avatar avatar--friend" role="img" aria-label="Ícono de perfil del amigo que responde" style="top:334px"></div>

      <p class="bubble bubble--reply" style="top:449px;height:48px">comportamientos de riesgo y falta de control de impulsos</p>
      <div class="avatar avatar--friend" role="img" aria-label="Ícono de perfil del amigo que responde" style="top:446px"></div>

      <p class="bubble bubble--reply" style="top:508px;height:82px">problemas de salud en la edad adulta: enfermedad cardíaca, presión arterial alta y dificultad para dormir.</p>
      <div class="avatar avatar--friend" role="img" aria-label="Ícono de perfil del amigo que responde" style="top:506px"></div>
    </div>
    <div class="phone__notch"><span class="phone__speaker"></span><span class="phone__camera"></span></div>
  </section>

  <section class="references">
    <h2 class="references__label">REFFERENCE</h2>
    <ul class="references__list">
      <li>https://www.bwr-example.org/kvtmpl/yrnq/articles/youth-risk-habits.html</li>
      <li>https://www.healthyminds-sample.org/pages/shared/docs/stayingclear_2.pdf</li>
      <li>https://www.healthyminds-sample.org/pages/shared/docs/stayingclear_2.pdf</li>
    </ul>
  </section>
</main>
</body>
</html>
```